Mechanical Engineer Business Card Design (Unemployed)

I am unemployed and actively looking for a job in Canada. I will be using this business card when I meet potential employers or in networking events.I would love to have the engraved writing style (as if it is engraved on the card). Some examples attached.I would love to have a personalized logo that represents my 2 majors. The final design should have a professional look that can stand out if attached to a resume. Jobs I am applying for are in construction, mining, oil and gas, Aerospace, manufacturing and whatever field I can be integrated in.A metallic look on the back is ok. but the front have to be sort of can be written on. you can also try to add my linkedin profile https://ca.folionet.example/in/doruvelsh
On the front or back, I would love to have the symbol of mail and phone rather than the words. that saves spaceAmaze me guys.

Target Market(s)

Engineering

Industry/Entity Type

Engineering

Contact Information for Business Card

Doru Velsh
Mechanical Engineer

Phone number: +1 (555) 014 - 2736
email: velshdoru@mailbrook.example

Font styles to use
Serif
Sans Serif
Decorative
Script

Requirements
Must have
• PERSONALIZED and brand new Simple Logo
• Professional look
• Engraved writing for the name
• Help stand out when attached on CV
Nice to have
• Metallic back look

```html
<!DOCTYPE html>
<html lang="en">
<head>
<meta charset="utf-8">
<title>Doru Velsh – Business Card Back</title>
<link rel="stylesheet" href="https://fonts.googleapis.com/css2?family=Lato:wght@300;400&display=swap">
<style>
  :root {
    --card-bg: #5e5e60;
    --ink: #ffffff;
  }
  html, body {
    margin: 0;
    padding: 0;
    width: 1200px;
    height: 702px;
    overflow: hidden;
    background: var(--card-bg);
  }
  .card {
    position: relative;
    width: 1200px;
    height: 702px;
    background: var(--card-bg);
    color: var(--ink);
    font-family: "Lato", "Helvetica Neue", Arial, sans-serif;
    font-weight: 300;
  }
  .icon {
    position: absolute;
    display: block;
  }
  .icon--mail { left: 382px; top: 238px; width: 102px; height: 74px; }
  .icon--phone { left: 384px; top: 350px; width: 88px; height: 88px; }
  .divider {
    position: absolute;
    left: 511px;
    top: 216px;
    width: 3px;
    height: 242px;
    background: var(--ink);
  }
  .contact {
    position: absolute;
    margin: 0;
    line-height: 1;
    white-space: nowrap;
  }
  .contact--email {
    left: 547px;
    top: 253px;
    font-size: 39px;
    letter-spacing: 4.2px;
  }
  .contact--phone {
    left: 558px;
    top: 375px;
    font-size: 37px;
    letter-spacing: 6.5px;
  }
</style>
</head>
<body>
  <main class="card">
    <svg class="icon icon--mail" viewBox="0 0 102 74" aria-label="Email" role="img">
      <rect x="2" y="5" width="98" height="67" rx="6" fill="none" stroke="#ffffff" stroke-width="3.5"/>
      <path d="M6 4 L51 38 L96 4" fill="none" stroke="#ffffff" stroke-width="3.5" stroke-linejoin="round"/>
      <path d="M12 4 L51 31 L90 4" fill="none" stroke="#ffffff" stroke-width="3" stroke-linejoin="round"/>
    </svg>
    <svg class="icon icon--phone" viewBox="0 0 88 88" aria-label="Phone" role="img">
      <path d="M20 4 C12 4 3 14 4 26 C6 46 22 68 44 80 C58 88 72 86 78 82 C86 77 87 70 83 65 L72 56 C68 53 63 54 60 58 L56 63 C52 66 46 64 40 58 C32 50 26 42 24 36 C22 30 26 27 30 24 L33 21 C36 18 36 14 34 11 L28 5 C26 4 23 3 20 4 Z" fill="none" stroke="#ffffff" stroke-width="3" stroke-linejoin="round"/>
    </svg>
    <div class="divider" aria-hidden="true"></div>
    <p class="contact contact--email">velshdoru@mailbrook.example</p>
    <p class="contact contact--phone">+1 (555) 014 - 2736</p>
  </main>
</body>
</html>
```